washable paper bags and accessories

We are three sisters who have discovered a mutual love of bags made from washable paper. It is a brand new business venture for bags, handbags, cosmetic bags, and home storage solutions and décor all made with washable paper.
We would like to have white crumpled paper as a background for both sides. Front of card with the words "plume douce cloth" only in "bohemian typewriter regular" font. Back of card with appointment style format for our next pop up stall
Target Market(s)
mums, females
Industry/Entity Type
Business
Contact Information for Business Card
ph: 0487215364
email:plumedoucecloth@mailbarrow.com

```html
<!DOCTYPE html>
<html lang="en">
<head>
<meta charset="utf-8">
<title>plume douce cloth — business card</title>
<link href="https://fonts.googleapis.com/css2?family=Special+Elite&display=swap" rel="stylesheet">
<style>
  :root {
    --backdrop: #f4f4f4;
    --paper-light: #ece8df;
    --paper-mid: #ddd8cc;
    --paper-shade: #cfcabe;
    --ink: #2b2a28;
  }
  * { margin: 0; padding: 0; box-sizing: border-box; }
  html, body {
    width: 1200px;
    height: 1000px;
    overflow: hidden;
    background: var(--backdrop);
  }
  .canvas {
    position: relative;
    width: 1200px;
    height: 1000px;
  }
  .card {
    position: absolute;
    top: 160px;
    width: 387px;
    height: 680px;
  }
  .card--front { left: 180px; }
  .card--back { left: 633px; }
  .card__paper {
    position: absolute;
    inset: 0;
    background:
      radial-gradient(ellipse at 30% 25%, var(--paper-light) 0%, transparent 60%),
      radial-gradient(ellipse at 70% 75%, var(--paper-light) 0%, transparent 55%),
      linear-gradient(160deg, var(--paper-mid) 0%, var(--paper-light) 45%, var(--paper-shade) 100%);
  }
  .brand-name {
    position: absolute;
    left: 0;
    right: 0;
    top: 302px;
    text-align: center;
    font-family: "Special Elite", "Courier New", monospace;
    font-size: 28px;
    letter-spacing: 1.5px;
    color: var(--ink);
  }
  .contact {
    position: absolute;
    left: 0;
    right: 0;
    text-align: center;
    color: var(--ink);
    font-family: "Special Elite", "Courier New", monospace;
  }
  .contact--phone { top: 274px; }
  .contact--email { top: 358px; }
  .contact__icon {
    display: block;
    margin: 0 auto 4px;
    width: 24px;
    height: 24px;
  }
  .contact__text { font-size: 19px; letter-spacing: 1px; }
  .contact--email .contact__text { font-size: 15px; letter-spacing: 0.5px; }
</style>
</head>
<body>
<main class="canvas">
  <section class="card card--front">
    <div class="card__paper" role="img" aria-label="White crumpled paper texture background"></div>
    <h1 class="brand-name">plume douce cloth</h1>
  </section>

  <section class="card card--back">
    <div class="card__paper" role="img" aria-label="White crumpled paper texture background"></div>

    <div class="contact contact--phone">
      <svg class="contact__icon" viewBox="0 0 24 24" aria-hidden="true">
        <circle cx="12" cy="12" r="12" fill="var(--ink)"/>
        <path d="M6 10c0-2 3-3 6-3s6 1 6 3v1h-3v-1.5h-6V11H6z" fill="none" stroke="#ece8df" stroke-width="1"/>
        <rect x="7.5" y="12" width="9" height="5" rx="1" fill="none" stroke="#ece8df" stroke-width="1"/>
        <circle cx="12" cy="14.5" r="1.3" fill="none" stroke="#ece8df" stroke-width="0.9"/>
      </svg>
      <p class="contact__text">0487215364</p>
    </div>

    <div class="contact contact--email">
      <svg class="contact__icon" viewBox="0 0 24 24" aria-hidden="true">
        <circle cx="12" cy="12" r="12" fill="var(--ink)"/>
        <rect x="6" y="8" width="12" height="8" fill="none" stroke="#ece8df" stroke-width="1.1"/>
        <path d="M6 8l6 5 6-5" fill="none" stroke="#ece8df" stroke-width="1.1"/>
      </svg>
      <p class="contact__text">plumedoucecloth@mailbarrow.com</p>
    </div>
  </section>
</main>
</body>
</html>
```